Blogging Membership Course Needs a Banner Ad Design

We need a banner ad design for a new membership site called Kitchen Scribe Institute which teaches food bloggers how to transform their blog into a full-time dream job through multimedia training modules and a private community.

We would like the design to use colors that are complementary to the attached logo design. The final design should be eye-catching without being obnoxious or "tacky." It should be simple, modern, clean, slightly feminine, and communicate dream-job, transformational business growth and learning (Kitchen Scribe *Institute*). Feel free to use the stock images attached or other images with proper disclosure.

See (rough) sales page here: http://kitchenscribeinstitute.example/home/

Designs should be 300x250.

Target Market(s)

Advanced food bloggers looking to finally take their blog to full-time status.

Industry/Entity Type

Training

Font styles to use
Sans Serif

Colors
33a6d7
00a890
f68d4d
faa54b
5c5c5c

Requirements
Must have
• Designs should be 300x250.
Should not have
• No spammy or clickbait-looking ads.

```html
<!DOCTYPE html>
<html lang="en">
<head>
<meta charset="utf-8">
<title>Kitchen Scribe Institute – Banner Ad</title>
<link rel="stylesheet" href="https://fonts.googleapis.com/css2?family=Courgette&family=Ubuntu:wght@500;700&display=swap">
<style>
  :root {
    --backdrop: #5b3c24;
    --chalk-green: #3f9f70;
    --chalk-green-dark: #2f8a5d;
    --accent-orange: #f2683c;
    --band-white: #ffffff;
    --text-white: #ffffff;
    --button-top: #7fd23a;
    --button-bottom: #3f9a12;
    --button-edge: #2f7a0c;
    --photo-warm: #e9c9a6;
    --photo-cool: #5aa985;
  }
  * { margin: 0; padding: 0; box-sizing: border-box; }
  html, body {
    width: 1200px;
    height: 757px;
    overflow: hidden;
    background: var(--backdrop);
  }
  .banner {
    position: absolute;
    left: 180px;
    top: 28px;
    width: 840px;
    height: 700px;
    overflow: hidden;
    background: var(--chalk-green);
    box-shadow: 0 6px 18px rgba(0,0,0,0.35);
  }
  .banner-shapes {
    position: absolute;
    inset: 0;
    width: 100%;
    height: 100%;
  }
  .hero-photo {
    position: absolute;
    left: 0;
    top: 0;
    width: 378px;
    height: 520px;
    background: radial-gradient(ellipse at 45% 40%, var(--photo-warm) 0%, #d9b07c 42%, var(--photo-cool) 82%);
  }
  .headline {
    position: absolute;
    left: 295px;
    top: 57px;
    width: 504px;
    text-align: center;
    font-family: "Courgette", cursive;
    font-weight: 400;
    font-size: 70px;
    line-height: 84px;
    color: var(--text-white);
    text-shadow: 0 2px 3px rgba(0,0,0,0.25);
    white-space: nowrap;
  }
  .subhead {
    position: absolute;
    left: 392px;
    top: 368px;
    width: 440px;
    font-family: "Ubuntu", sans-serif;
    font-weight: 500;
    font-size: 46px;
    line-height: 59px;
    color: var(--text-white);
    white-space: nowrap;
  }
  .subhead strong { font-weight: 700; }
  .brand-name {
    position: absolute;
    left: 40px;
    top: 560px;
    width: 340px;
    font-family: "Ubuntu", sans-serif;
    font-weight: 700;
    font-size: 36px;
    line-height: 42px;
    color: var(--accent-orange);
    text-transform: uppercase;
    text-align: center;
  }
  .cta-button {
    position: absolute;
    left: 428px;
    top: 582px;
    width: 384px;
    height: 87px;
    border-radius: 44px;
    background: linear-gradient(to bottom, var(--button-top), var(--button-bottom));
    border: 3px solid var(--button-edge);
    font-family: "Ubuntu", sans-serif;
    font-weight: 700;
    font-size: 36px;
    color: var(--text-white);
    display: flex;
    align-items: center;
    padding-left: 42px;
    text-shadow: 0 2px 2px rgba(0,0,0,0.3);
  }
  .cta-arrow {
    position: absolute;
    right: 10px;
    top: 50%;
    width: 60px;
    height: 60px;
    margin-top: -30px;
    border-radius: 50%;
    background: var(--band-white);
    display: flex;
    align-items: center;
    justify-content: center;
  }
</style>
</head>
<body>
  <div class="banner">
    <svg class="banner-shapes" viewBox="0 0 300 250" preserveAspectRatio="none" aria-hidden="true">
      <rect width="300" height="250" fill="var(--chalk-green)"/>
      <rect x="0" y="0" width="300" height="90" fill="var(--chalk-green-dark)" opacity="0.25"/>
    </svg>

    <div class="hero-photo" role="img" aria-label="Photo of a smiling young woman with long blonde hair in a coral top"></div>

    <svg class="banner-shapes" viewBox="0 0 300 250" preserveAspectRatio="none" aria-hidden="true">
      <path d="M0 174 Q150 176 300 180 L300 190 Q150 186 0 188 Z" fill="var(--accent-orange)"/>
      <path d="M0 186 Q150 184 300 188 L300 250 L0 250 Z" fill="var(--band-white)"/>
    </svg>

    <h1 class="headline">Turn Your blog<br>into Your<br>dream job!</h1>

    <p class="subhead">Make a living doing<br>what you <strong>LOVE!</strong></p>

    <div class="brand-name">Kitchen Scribe<br>Institute</div>

    <div class="cta-button">Learn More!
      <span class="cta-arrow">
        <svg width="26" height="30" viewBox="0 0 26 30" aria-hidden="true">
          <path d="M7 4 L19 15 L7 26" fill="none" stroke="var(--button-bottom)" stroke-width="6" stroke-linecap="round" stroke-linejoin="round"/>
        </svg>
      </span>
    </div>
  </div>
</body>
</html>
```